Business Card for Coach - ready to print

Design Business Card ready to order prints www.lukasbrenner.coach

* An Overview / Background of the Business & Services
· Coaching
· Personal growth
* The Target Market / Audience you are trying to reach
· private person in different roles (self, familiy, business role)s
* Design Specifics; any preferences or ideas for Style, Colour, Imagery, etc
· See www.lukasbrenner.coach
· "simple" design
· (small) element of surprise / unusual element

* Information that will be placed in the Business Card
· Beratung und Coaching
· Address: Lukas Brenner, Talmatt 42, CH-8531 Winterthur, Mobile +41 76 254 63 07
* Do you have an existing website or Friendspace page where designers can learn more about your company?
· lukasbrenner.coach

Target Market(s)

private person in different roles (self, familiy, business role)

Industry/Entity Type

Life Coaching

Contact Information for Business Card

Lukas Brenner
Talmatt 42
CH-8531 Winterthur

Mobile: +41 76 254 63 07
Email: lubr@sonnwelt.ch
www.lukasbrenner.coach

Font styles to use
Sans Serif

Colors

Designer to choose colors to be used in the design.

Requirements
Must have
• "simple" design
• element of surprise / unusual element
• Beratung & Coaching
• see www.lukasbrenner.coach for colors and so...
Nice to have
• TA Symbol (three rings on top of each other) - unsual presentation
• QR Code of Website (see if it fits in and still looks good).

```html
<!DOCTYPE html>
<html lang="de">
<head>
<meta charset="utf-8">
<title>Beratung &amp; Coaching – Visitenkarte</title>
<link rel="stylesheet" href="https://fonts.googleapis.com/css2?family=Open+Sans:wght@300;400;600;700&display=swap">
<style>
  :root {
    --bg: #e9e7e4;
    --card: #ffffff;
    --sky: #bde2f5;
    --ink: #8a8a8a;
    --ink-strong: #7a7a7a;
    --rule: #a9a9a9;
  }
  * { box-sizing: border-box; margin: 0; padding: 0; }
  html, body { width: 1200px; height: 794px; overflow: hidden; }
  body {
    background: var(--bg);
    font-family: "Open Sans", Arial, sans-serif;
    color: var(--ink);
    position: relative;
  }
  .card {
    position: absolute;
    top: 229px;
    width: 520px;
    height: 336px;
    background: var(--card);
    box-shadow: 0 6px 18px rgba(0,0,0,.12);
  }
  .card--front { left: 50px; }
  .card--back { left: 630px; }

  .front-panel {
    position: absolute;
    inset: 22px;
    background: var(--sky);
  }
  .front-title {
    position: absolute;
    left: 48px;
    bottom: 82px;
    font-size: 44px;
    font-weight: 400;
    letter-spacing: .5px;
    color: var(--ink);
    white-space: nowrap;
  }

  .contact {
    position: absolute;
    left: 262px;
    top: 26px;
    font-size: 13px;
    line-height: 1.5;
    color: var(--ink);
  }
  .contact-name { font-size: 17px; margin-bottom: 4px; }
  .contact-name strong { font-weight: 700; color: var(--ink-strong); }
  .contact-line { display: flex; align-items: center; gap: 8px; }
  .contact-line svg { width: 11px; height: 11px; flex: none; }
  .contact-address { margin-top: 8px; }

  .frame-rule {
    position: absolute;
    left: 30px;
    top: 168px;
    width: 332px;
    height: 156px;
    border-top: 5px solid var(--rule);
    border-right: 5px solid var(--rule);
  }
  .message {
    position: absolute;
    left: 22px;
    top: 178px;
    width: 330px;
    height: 136px;
    background: var(--sky);
    padding: 18px 22px;
    font-size: 13.5px;
    line-height: 1.5;
    color: var(--ink);
  }
  .message-title { font-weight: 700; color: var(--ink-strong); margin-bottom: 4px; }
  .message p { word-spacing: 3px; }
  .message strong { font-weight: 700; color: var(--ink-strong); }
</style>
</head>
<body>
  <section class="card card--front" aria-label="Vorderseite">
    <div class="front-panel"></div>
    <h1 class="front-title">Beratung &amp; Coaching</h1>
  </section>

  <section class="card card--back" aria-label="Rückseite">
    <div class="contact">
      <div class="contact-name"><strong>Lukas</strong> Brenner</div>
      <div class="contact-line">
        <svg viewBox="0 0 12 12" aria-hidden="true"><rect x="2.5" y="0.8" width="7" height="10.4" rx="1.2" fill="none" stroke="#8a8a8a" stroke-width="1.2"/><circle cx="6" cy="9.3" r=".7" fill="#8a8a8a"/></svg>
        <span>+41 76 254 63 07</span>
      </div>
      <div class="contact-line">
        <svg viewBox="0 0 12 12" aria-hidden="true"><rect x="0.5" y="2" width="11" height="8" fill="#8a8a8a"/><path d="M0.8 2.4 6 6.6 11.2 2.4" fill="none" stroke="#fff" stroke-width="1"/></svg>
        <span>lubr@sonnwelt.ch</span>
      </div>
      <div class="contact-line">
        <svg viewBox="0 0 12 12" aria-hidden="true"><circle cx="6" cy="6" r="5.3" fill="#8a8a8a"/><path d="M0.8 6h10.4M6 .7c-2.6 2.8-2.6 7.8 0 10.6M6 .7c2.6 2.8 2.6 7.8 0 10.6" fill="none" stroke="#fff" stroke-width=".8"/></svg>
        <span>www.lukasbrenner.coach</span>
      </div>
      <div class="contact-address">
        <div>Talmatt 42</div>
        <div>CH-8531 Winterthur</div>
      </div>
    </div>

    <div class="frame-rule"></div>
    <div class="message">
      <div class="message-title">Beratung &amp; Coaching</div>
      <p>Do you have an existing <strong>website</strong> or <strong>Friendspace</strong> page where designers can learn more about your company?</p>
    </div>
  </section>
</body>
</html>
```